Varro's Electrical & Solar Corflute Signage Design

So my plan is to put this design onto a 600 by 400 corflute sign (this sign will be printed out and cable tied to a fence FYI). I would like to have the name and the icon stand out. I need Varro's Electrical & Solar to be big and clear and I would like to have my "S" icon faded behind "Varro's Electrical & Solar" in the background.

I want to have my Lic No. - Top left with my ABN directly underneath. (I Want two ticks infront of them like this)
✓ Lic No. 582164K
✓ ABN 41 276 519 683

I want to have written on it: ALL ASPECTS OF ELECTRICAL (please use cool fonts and nothing too plain)
I also want to have: YOUR LOCAL TRUSTED ELECTRICIAN but if it looks too dicky then just have "all aspects of electrical" and just "free quotes • fast service" somewhere.
Directly underneath (smaller but still clear): FREE QUOTES • FAST SERVICE

At the bottom, I need my phone number big and clear - 0438 617 905 I would like this on a banner meaning like a cool strip at the bottom. (Please make the strip/banner look cool and not boring. Maybe shade the colour or something)
I also want the Facebook & Instagram icons on there so people can look us up on facebook & Instagram (make them match the colour of my logo or you could try any other colour that works)
Thank you so much!!

Colors

Designer to choose colors to be used in the design.

Requirements
Should not have
• no different colours other then the colours on my logo and icon

```html
<!DOCTYPE html>
<html lang="en">
<head>
<meta charset="utf-8">
<title>Varro's Electrical &amp; Solar – Corflute Sign</title>
<link rel="stylesheet" href="https://fonts.googleapis.com/css2?family=Oswald:wght@500;700&family=Russo+One&family=Montserrat:wght@700;800&display=swap">
<style>
  :root{
    --green:#4fb82a;
    --green-light:#7ad83f;
    --green-dark:#2a7a17;
    --black:#0d0f0d;
    --charcoal:#1c201c;
    --white:#ffffff;
    --ink:#111311;
    --backdrop:#a7c0a6;
  }
  *{box-sizing:border-box;margin:0;padding:0}
  html,body{width:891px;height:1200px;overflow:hidden;background:var(--backdrop)}
  .sign{
    position:absolute;left:20px;top:316px;width:851px;height:567px;
    background:var(--white);overflow:hidden;
    box-shadow:0 10px 30px rgba(0,0,0,.25);
    font-family:"Montserrat",sans-serif;
  }
  .sign__top{
    position:absolute;left:0;top:0;width:100%;height:240px;
    background:radial-gradient(ellipse at 50% 35%,var(--charcoal),var(--black) 75%);
  }
  .sign__stripes{position:absolute;left:0;top:0;width:100%;height:240px}
  .credentials{position:absolute;left:0;top:16px;display:flex;flex-direction:column;gap:8px;z-index:2}
  .credentials__item{
    display:flex;align-items:center;gap:8px;height:30px;padding:0 26px 0 12px;
    background:linear-gradient(90deg,var(--green-dark),var(--green));
    clip-path:polygon(0 0,100% 0,calc(100% - 14px) 100%,0 100%);
    color:var(--white);font-weight:800;font-size:15px;letter-spacing:.5px;
  }
  .credentials__tick{width:20px;height:20px;flex:none}
  .brand{position:absolute;left:0;top:20px;width:100%;text-align:center;color:var(--green-light);font-family:"Russo One",sans-serif;font-weight:400}
  .brand__name{font-size:74px;line-height:1;letter-spacing:3px}
  .brand__sub{font-size:20px;letter-spacing:6px;margin-top:4px}
  .headline{
    position:absolute;left:0;top:146px;width:100%;text-align:center;white-space:nowrap;
    font-family:"Oswald",sans-serif;font-weight:700;font-size:64px;line-height:1;
    color:var(--white);letter-spacing:0;
  }
  .tagline{
    position:absolute;left:70px;top:240px;width:711px;height:46px;
    background:linear-gradient(90deg,var(--green-dark),var(--green) 25%,var(--green) 75%,var(--green-dark));
    clip-path:polygon(0 0,100% 0,calc(100% - 26px) 100%,26px 100%);
    display:flex;align-items:center;justify-content:center;
    color:var(--white);font-weight:800;font-size:25px;letter-spacing:3px;
  }
  .tagline-edge{position:absolute;top:240px;height:46px;width:100px;background:var(--black)}
  .tagline-edge--left{left:0;clip-path:polygon(0 0,100% 0,70% 100%,0 100%)}
  .tagline-edge--right{right:0;clip-path:polygon(0 0,100% 0,100% 100%,30% 100%)}
  .offers{position:absolute;left:0;top:308px;width:100%;display:flex;justify-content:center;gap:40px}
  .offer{
    display:flex;align-items:center;gap:12px;height:50px;padding:0 26px 0 6px;
    border:3px solid var(--green);border-radius:28px;
    font-weight:800;font-size:24px;color:var(--ink);letter-spacing:.5px;
  }
  .offer__icon{width:38px;height:38px;flex:none}
  .phone{position:absolute;left:0;top:376px;width:100%;display:flex;justify-content:center;align-items:center;gap:18px}
  .phone__icon{width:72px;height:72px;flex:none}
  .phone__number{font-family:"Oswald",sans-serif;font-weight:700;font-size:88px;line-height:1;color:var(--ink);letter-spacing:1px}
  .social{
    position:absolute;left:0;bottom:0;width:100%;height:52px;
    background:linear-gradient(90deg,var(--green-dark) 20%,var(--green) 45%,var(--green-dark));
    clip-path:polygon(22% 0,100% 0,100% 100%,19% 100%);
    display:flex;align-items:center;justify-content:flex-end;gap:12px;padding-right:30px;
  }
  .social__label{color:var(--white);font-weight:800;font-size:18px;letter-spacing:4px;margin-right:8px}
  .social__dot{width:30px;height:30px;border-radius:50%;background:var(--white)}
</style>
</head>
<body>
  <section class="sign" aria-label="Varro's Electrical & Solar sign">
    <div class="sign__top"></div>
    <svg class="sign__stripes" viewBox="0 0 851 240" aria-hidden="true">
      <g stroke="#4fb82a" stroke-width="6" opacity=".55">
        <line x1="700" y1="240" x2="851" y2="60"/>
        <line x1="740" y1="240" x2="851" y2="110"/>
        <line x1="780" y1="240" x2="851" y2="160"/>
        <line x1="0" y1="200" x2="60" y2="130"/>
        <line x1="0" y1="240" x2="90" y2="135"/>
      </g>
    </svg>

    <div class="credentials">
      <div class="credentials__item">
        <svg class="credentials__tick" viewBox="0 0 20 20" aria-hidden="true"><circle cx="10" cy="10" r="9" fill="#0d0f0d"/><path d="M5 10.5l3.2 3L15 6.5" fill="none" stroke="#7ad83f" stroke-width="2.6" stroke-linecap="round" stroke-linejoin="round"/></svg>
        LIC NO. 582164K
      </div>
      <div class="credentials__item">
        <svg class="credentials__tick" viewBox="0 0 20 20" aria-hidden="true"><circle cx="10" cy="10" r="9" fill="#0d0f0d"/><path d="M5 10.5l3.2 3L15 6.5" fill="none" stroke="#7ad83f" stroke-width="2.6" stroke-linecap="round" stroke-linejoin="round"/></svg>
        ABN 41 276 519 683
      </div>
    </div>

    <div class="brand">
      <div class="brand__name">VARRO'S</div>
      <div class="brand__sub">ELECTRICAL &amp; SOLAR</div>
    </div>

    <h1 class="headline">ALL ASPECTS OF ELECTRICAL</h1>

    <div class="tagline-edge tagline-edge--left"></div>
    <div class="tagline-edge tagline-edge--right"></div>
    <div class="tagline">YOUR LOCAL TRUSTED ELECTRICIAN</div>

    <div class="offers">
      <div class="offer">
        <svg class="offer__icon" viewBox="0 0 38 38" aria-hidden="true"><circle cx="19" cy="19" r="16" fill="none" stroke="#4fb82a" stroke-width="3"/><text x="19" y="26" text-anchor="middle" font-family="Montserrat,sans-serif" font-weight="800" font-size="20" fill="#111311">$</text></svg>
        FREE QUOTES
      </div>
      <div class="offer">
        <svg class="offer__icon" viewBox="0 0 38 38" aria-hidden="true"><circle cx="20" cy="21" r="13" fill="none" stroke="#4fb82a" stroke-width="3"/><path d="M20 13v8l5 4" fill="none" stroke="#111311" stroke-width="3" stroke-linecap="round"/><line x1="16" y1="5" x2="24" y2="5" stroke="#111311" stroke-width="3" stroke-linecap="round"/><line x1="2" y1="16" x2="8" y2="16" stroke="#4fb82a" stroke-width="2.5" stroke-linecap="round"/><line x1="1" y1="22" x2="6" y2="22" stroke="#4fb82a" stroke-width="2.5" stroke-linecap="round"/></svg>
        FAST SERVICE
      </div>
    </div>

    <div class="phone">
      <svg class="phone__icon" viewBox="0 0 72 72" aria-hidden="true">
        <circle cx="36" cy="36" r="34" fill="#4fb82a"/>
        <path d="M25 18c2-1 4 0 5 2l3 7c1 2 0 4-1 5l-3 2c2 5 6 9 11 11l2-3c1-1 3-2 5-1l7 3c2 1 3 3 2 5l-2 5c-1 2-3 3-5 3-16-1-29-14-30-30 0-2 1-4 3-5z" fill="#ffffff"/>
      </svg>
      <div class="phone__number">0438 617 905</div>
    </div>

    <footer class="social">
      <span class="social__label">FOLLOW US ON</span>
      <span class="social__dot"></span>
      <span class="social__dot"></span>
    </footer>
  </section>
</body>
</html>
```